Brightmere Realty information card

We need a 5x7 two-sided card to hand out at open houses and provide to our charitable partners for distribution. We are a local real estate group looking to add a "give back" component to our business. We are located in a coastal community and would like to incorporate that feel into our design. We are giving clients who use us the ability to designate 1 out of the 10 charitable organizations we partner with - and we will make a donation to that organization.

We included the 10 partner logos below - we envision them pretty small. Also included 2 photos of the "Brightmere" and our logo. Have fun.
Updates

Project Deadline Extended
Reason: We're out of town until Wednesday, May 17th.

Target Market(s)

home buyers & sellers

Industry/Entity Type

Real Estate

Font styles to use
Serif
Sans Serif

Colors

Designer to choose colors to be used in the design.

Requirements
Must have
• slogan & tagline - see attached text file
• Brightmere photo
Nice to have
• partner logos - small - maybe in circles?

```html
<!DOCTYPE html>
<html lang="en">
<head>
<meta charset="utf-8">
<title>Brightmere Realty – Information Card</title>
<link href="https://fonts.googleapis.com/css2?family=Open+Sans:ital,wght@0,400;0,600;0,700;1,600;1,700&family=Noto+Serif:ital@1&display=swap" rel="stylesheet">
<style>
  :root{
    --page:#ffffff;
    --blue-deep:#0a3f9e;
    --blue-band:#0c52c8;
    --blue-mid:#3f86e6;
    --blue-sky:#6fa6ea;
    --accent:#4a8ef0;
    --white:#ffffff;
    --sunset-top:#e8805a;
    --sunset-mid:#d9664f;
    --city-dark:#2a2230;
  }
  *{margin:0;padding:0;box-sizing:border-box}
  html,body{width:927px;height:1200px;overflow:hidden;background:var(--page)}
  body{position:relative;font-family:"Open Sans",Arial,sans-serif;color:var(--white)}

  .card{position:absolute;left:82px;width:765px;overflow:hidden;box-shadow:3px 4px 6px rgba(0,0,0,.35)}
  .card svg.backdrop{position:absolute;inset:0}

  /* front */
  .card--front{top:45px;height:547px}
  .brand{position:absolute;left:24px;top:98px;width:270px;text-align:center;
    font-weight:600;font-size:46px;line-height:58px;color:var(--white)}
  .tagline{position:absolute;right:34px;font-family:"Noto Serif",Georgia,serif;font-style:italic;
    font-size:20.5px;color:var(--white);white-space:nowrap}
  .tagline--first{top:126px}
  .tagline--second{top:163px}
  .rule{position:absolute;right:0;height:2px;background:var(--accent)}
  .rule--first{top:157px;left:423px}
  .rule--second{top:193px;left:358px}
  .pledge{position:absolute;left:383px;top:221px;width:348px;font-size:11.6px;line-height:19.8px;text-align:justify}

  /* back */
  .card--back{top:611px;height:546px}
  .message{position:absolute;left:43px;top:26px;width:681px;font-size:16.6px;line-height:25.8px;
    font-weight:600;text-align:justify}
  .message .lead{font-style:italic;font-weight:700;display:block}
  .message p{margin:0}
  .partners{position:absolute;left:15px;top:293px;display:flex;gap:13.2px}
  .partner{width:61px;height:61px;border-radius:50%;border:2px solid var(--white)}
  .site{position:absolute;left:0;right:0;top:388px;text-align:center;font-weight:700;font-size:24px;letter-spacing:5.2px}
  .contacts{position:absolute;left:44px;top:437px;font-size:17px;line-height:26px}
</style>
</head>
<body>

<section class="card card--front">
  <svg class="backdrop" width="765" height="547" viewBox="0 0 765 547">
    <defs>
      <linearGradient id="skyBlue" x1="0" y1="0" x2="1" y2="0">
        <stop offset="0" stop-color="#1e5bc4"/>
        <stop offset=".5" stop-color="#5a9af0"/>
        <stop offset="1" stop-color="#1a55c0"/>
      </linearGradient>
      <linearGradient id="sunsetScene" x1="0" y1="0" x2="0" y2="1">
        <stop offset="0" stop-color="#8a8fb8"/>
        <stop offset=".2" stop-color="var(--sunset-top)"/>
        <stop offset=".45" stop-color="var(--sunset-mid)"/>
        <stop offset=".62" stop-color="#8a4a55"/>
        <stop offset=".8" stop-color="#3b2f3d"/>
        <stop offset="1" stop-color="var(--city-dark)"/>
      </linearGradient>
    </defs>
    <rect width="765" height="547" fill="url(#skyBlue)"/>
    <path role="img" aria-label="Photo of the coastal town at sunset, bay and pier under an orange sky"
      d="M0 40 C 200 0, 420 30, 560 75 C 640 98, 710 104, 765 102 L765 547 L0 547 Z" fill="url(#sunsetScene)"/>
    <path d="M0 40 C 200 0, 420 30, 560 75 C 640 98, 710 104, 765 102" fill="none" stroke="var(--white)" stroke-width="5"/>
  </svg>
  <div class="brand">Brightmere<br>Realty</div>
  <div class="tagline tagline--first">Change Homes, Change Lives</div>
  <div class="rule rule--first"></div>
  <div class="tagline tagline--second">Changing the World One Home at a Time</div>
  <div class="rule rule--second"></div>
  <p class="pledge">Because we value generosity and desire to make a difference in our community and world, for every home bought or sold through us, we will make a contribution to one of our amazing partner who are helping to change the world.</p>
</section>

<section class="card card--back">
  <svg class="backdrop" width="765" height="546" viewBox="0 0 765 546">
    <defs>
      <linearGradient id="backSky" x1="0" y1="0" x2="0" y2="1">
        <stop offset="0" stop-color="#5e98e8"/>
        <stop offset="1" stop-color="var(--blue-sky)"/>
      </linearGradient>
      <linearGradient id="footWave" x1="0" y1="0" x2="1" y2="0">
        <stop offset="0" stop-color="#2a6ad6"/>
        <stop offset=".5" stop-color="var(--blue-deep)"/>
        <stop offset="1" stop-color="#0b3c94"/>
      </linearGradient>
    </defs>
    <rect role="img" aria-label="Soft blue sky photo behind the message" width="765" height="275" fill="url(#backSky)"/>
    <rect y="275" width="765" height="95" fill="var(--blue-band)"/>
    <rect role="img" aria-label="Faded aerial view of the town" y="370" width="765" height="176" fill="#4a82d4"/>
    <path d="M0 505 C 180 540, 420 520, 560 470 C 650 440, 720 428, 765 423 L765 546 L0 546 Z" fill="url(#footWave)"/>
    <path d="M0 505 C 180 540, 420 520, 560 470 C 650 440, 720 428, 765 423" fill="none" stroke="var(--white)" stroke-width="4"/>
  </svg>
  <div class="message">
    <span class="lead">We live here.&nbsp; We give here.</span>
    <p>We give because we value generosity and believe we have been blessed to be a blessing.&nbsp; We believe that together we can change the world one home at time.&nbsp; You have our guarantee of personal service and no additional costs.&nbsp; The donations come out of our commission, not your pocket.&nbsp; You get to designate which of our amazing partner organizations you would like us to contribute to on behalf of your transaction.</p>
    <p>When you are ready to buy or sell, please consider giving us a call.&nbsp; Tell a friend about us too.&nbsp; Together, we can make the world a better place.</p>
  </div>
  <div class="partners" role="list" aria-label="Partner organizations">
    <span class="partner" role="listitem" style="background:#e9e6ee"></span>
    <span class="partner" role="listitem" style="background:#6d7a58"></span>
    <span class="partner" role="listitem" style="background:#5a3a2a"></span>
    <span class="partner" role="listitem" style="background:#000000"></span>
    <span class="partner" role="listitem" style="background:#ffffff"></span>
    <span class="partner" role="listitem" style="background:#d8202a"></span>
    <span class="partner" role="listitem" style="background:#ffffff"></span>
    <span class="partner" role="listitem" style="background:#ffffff"></span>
    <span class="partner" role="listitem" style="background:#e48cc8"></span>
    <span class="partner" role="listitem" style="background:#ffffff"></span>
  </div>
  <div class="site">brightmererealty.com</div>
  <div class="contacts">
    Evan Marlowe : evan@brightmererealty.com<br>
    Jenna Marlowe : jenna@brightmererealty.com
  </div>
</section>

</body>
</html>
```